Geschäftspapiere für eine Zahnarztpraxis
Zielgruppe
Zahnarztpraxis
Aufgabenstellung
Ich wünsche mir wenige grafische Elemente auf der Vorderseite. Die Rückseite soll komplett mit einer Grafik gefüllt sein.
Die Datei die ich als Fototapete zur Verfügung stelle, muss nicht zwangsläufig in dem Designvorschlag enthalten sein. Die Tapeten machen einen Großteil der Inneneinrichtung meiner Praxis aus. Sie sind ein Wiedererkennungsmerkmal, daher dachte ich, es würde Sinn ergeben, diese zum Teil in das Design einfließen zu lassen.

```html
<!DOCTYPE html>
<html lang="de">
<head>
<meta charset="utf-8">
<title>Geschäftspapiere – Zahnarztpraxis Lindqvist &amp; Team</title>
<link href="https://fonts.googleapis.com/css2?family=Manrope:wght@400;500;700&display=swap" rel="stylesheet">
<style>
  :root{
    --backdrop:#638c86;
    --paper:#ffffff;
    --teal:#4e8076;
    --text:#5a5f5e;
    --rule:#8aa9a3;
    --wash:linear-gradient(135deg,#e3c0b4 0%,#a9c2bb 35%,#e6c79a 58%,#b2a6c9 78%,#7fa69d 100%);
    --wash-cool:linear-gradient(135deg,#cdbfcd 0%,#9dbab3 50%,#79a297 100%);
  }
  *{margin:0;padding:0;box-sizing:border-box}
  html,body{width:1200px;height:1200px;overflow:hidden}
  body{background:var(--backdrop);font-family:"Manrope",sans-serif;position:relative}

  .sheet{position:absolute;background:var(--paper);box-shadow:0 2px 6px rgba(0,0,0,.18);overflow:hidden}
  .letterhead{left:347px;top:50px;width:780px;height:1102px}
  .card{width:316px;height:204px;left:73px}
  .card-front{top:334px}
  .card-back{top:574px}

  .wallpaper{position:absolute;background:var(--wash)}
  .wallpaper.cool{background:var(--wash-cool)}

  .brand{position:absolute;color:var(--teal);text-transform:uppercase;font-weight:400;line-height:1.1}
  .brand .sub{display:block;letter-spacing:.02em}
  .brand .name{display:block;letter-spacing:.04em}
  .brand-mark{position:absolute;border:2px solid var(--teal);border-radius:50%}

  .letterhead .brand-mark{left:78px;top:84px;width:62px;height:62px}
  .letterhead .brand{left:153px;top:98px}
  .letterhead .brand .sub{font-size:18px;margin-left:40px}
  .letterhead .brand .name{font-size:22px;margin-top:2px}

  .fold-mark{position:absolute;left:0;top:779px;width:22px;height:1px;background:var(--rule)}

  .footer{position:absolute;left:0;right:0;top:1034px;font-size:8.4px;line-height:1.38;color:var(--text)}
  .footer-col{position:absolute;top:0}
  .footer-col h4{font-size:8.4px;font-weight:700;color:var(--teal);text-transform:uppercase;letter-spacing:.03em}
  .footer-col .lead{color:var(--teal);text-transform:uppercase}
  .footer-col .lead strong{font-weight:700}
  .col-address{left:74px}
  .col-contact{left:211px}
  .col-bank{left:408px}
  .col-hours{left:615px}
  .footer-divider{position:absolute;left:605px;top:1024px;bottom:0;width:1px;background:var(--rule)}

  .card-front .brand-mark{left:86px;top:100px;width:38px;height:38px}
  .card-front .brand{left:0;width:210px;top:146px;text-align:center}
  .card-front .brand .sub{font-size:12px}
  .card-front .brand .name{font-size:14.5px;margin-top:2px}

  .card-back .details{position:absolute;left:19px;top:28px;color:var(--text);font-size:10.2px;line-height:1.3}
  .card-back .brand{position:static}
  .card-back .brand .sub{font-size:14px;letter-spacing:.01em}
  .card-back .brand .name{font-size:14.5px;font-weight:700;letter-spacing:.01em;margin-top:2px}
  .card-back p{margin-top:1px}
  .card-back .gap{margin-top:13px}
  .card-back .web{font-weight:700}
  .card-back h4{font-size:10.2px;font-weight:700;color:var(--teal);text-transform:uppercase;letter-spacing:.03em;margin-top:13px}
</style>
</head>
<body>

<section class="sheet letterhead">
  <div class="wallpaper cool" role="img" aria-label="Aquarell-Tapete der Praxis" style="left:0;top:0;width:55px;height:110px"></div>
  <div class="wallpaper cool" role="img" aria-label="Aquarell-Tapete der Praxis" style="left:175px;top:0;width:105px;height:60px"></div>
  <div class="wallpaper" role="img" aria-label="Aquarell-Tapete der Praxis in Teal, Rosé, Gelb und Violett" style="left:420px;top:0;width:360px;height:160px"></div>
  <div class="wallpaper" role="img" aria-label="Aquarell-Tapete der Praxis in Teal, Rosé, Gelb und Violett" style="left:670px;top:160px;width:110px;height:310px"></div>

  <span class="brand-mark"></span>
  <div class="brand">
    <span class="sub">Zahnarztpraxis</span>
    <span class="name">Lindqvist &amp; Team</span>
  </div>

  <span class="fold-mark"></span>

  <div class="footer">
    <div class="footer-col col-address">
      <div class="lead">Zahnarztpraxis<br><strong>Lindqvist &amp; Team</strong></div>
      Lindenallee 14<br>48291 Ostervelde
    </div>
    <div class="footer-col col-contact">
      <h4>Kontakt:</h4>
      Telefon 05123 48760<br>info@zahnarztpraxis-ostervelde.de<br>www.zahnarztpraxis-ostervelde.de
    </div>
    <div class="footer-col col-bank">
      <h4>Bankverbindung:</h4>
      IBAN: DE00 0000 0000 0000 0000 00<br>BIC: DEXXXXXXXXX<br>St.-Nr.: 000/000/0000
    </div>
    <div class="footer-col col-hours">
      <h4>Öffnungszeiten:</h4>
      Mo, Mi, Do 08:00 bis 18:30 Uhr<br>Di, Fr 08:00 bis 13:30 Uhr
    </div>
  </div>
  <span class="footer-divider"></span>
</section>

<section class="sheet card card-front">
  <div class="wallpaper" role="img" aria-label="Aquarell-Tapete der Praxis in Teal, Rosé, Gelb und Violett" style="left:0;top:0;width:316px;height:60px"></div>
  <div class="wallpaper" role="img" aria-label="Aquarell-Tapete der Praxis in Teal, Rosé, Gelb und Violett" style="left:230px;top:60px;width:86px;height:144px"></div>
  <span class="brand-mark"></span>
  <div class="brand">
    <span class="sub">Zahnarztpraxis</span>
    <span class="name">Lindqvist &amp; Team</span>
  </div>
</section>

<section class="sheet card card-back">
  <div class="wallpaper cool" role="img" aria-label="Aquarell-Tapete der Praxis" style="left:175px;top:164px;width:141px;height:40px"></div>
  <div class="details">
    <div class="brand">
      <span class="sub">Zahnarztpraxis</span>
      <span class="name">Lindqvist &amp; Team</span>
    </div>
    <p>Lindenallee 14, 48291 Ostervelde</p>
    <p class="gap">Tel.: 05123 48760 | info@zahnarztpraxis-ostervelde.de</p>
    <p class="web">www.zahnarztpraxis-ostervelde.de</p>
    <h4>Öffnungszeiten:</h4>
    <p>Mo, Mi, Do 08:00 - 18:30 Uhr<br>Di, Fr 08:00 - 13:30 Uhr</p>
  </div>
</section>

</body>
</html>
```